Postcard Design Project

I am an answering service and appointment scheduler for various Real Estate Appraisers around the country. This is for soliciting new clients.

Industry/Entity Type

Real Estate

```html
<!DOCTYPE html>
<html lang="en">
<head>
<meta charset="utf-8">
<title>The Valuation Desk – Postcard</title>
<link rel="stylesheet" href="https://fonts.googleapis.com/css2?family=Pathway+Gothic+One&display=swap">
<style>
  :root {
    --maroon: #860000;
    --maroon-deep: #5e0000;
    --cream: #f7f9a8;
    --gold: #ffe81a;
    --white: #ffffff;
    --ink: #111111;
    --offer-red: #ff1a1a;
    --silver-light: #e4ecec;
    --silver-dark: #7d8f8f;
    --dot: #d9d9d9;
    --stamp: #ececec;
    --condense: 0.87;
  }
  * { margin: 0; padding: 0; box-sizing: border-box; }
  html, body { width: 1200px; height: 930px; overflow: hidden; background: var(--white); }
  .postcard {
    position: relative;
    width: 1200px;
    height: 930px;
    font-family: "Pathway Gothic One", "Arial Narrow", sans-serif;
    overflow: hidden;
    background: var(--white);
  }
  .postcard__backdrop { position: absolute; inset: 0; }

  .pitch {
    position: absolute;
    left: 41px;
    top: 38px;
    color: var(--white);
    font-size: 31px;
    line-height: 42.5px;
    letter-spacing: -0.2px;
    white-space: nowrap;
    transform: scaleX(var(--condense));
    transform-origin: left top;
  }
  .pitch__lead { color: var(--gold); }

  .services-heading {
    position: absolute;
    left: 0;
    top: 287px;
    width: 365px;
    height: 38px;
    background: radial-gradient(ellipse 60% 70% at 55% 50%, var(--cream) 55%, rgba(247,249,168,0.55) 80%, rgba(247,249,168,0) 100%);
    color: var(--ink);
    font-size: 34px;
    font-weight: 400;
    line-height: 38px;
    padding-left: 67px;
    letter-spacing: 0.5px;
  }

  .services {
    position: absolute;
    left: 33px;
    top: 330px;
    list-style: none;
  }
  .services__item {
    display: flex;
    align-items: center;
    height: 42.6px;
  }
  .services__dot {
    width: 14px;
    height: 14px;
    border-radius: 50%;
    background: radial-gradient(circle at 40% 35%, #ffffe0, #e4e38c 60%, #9c9a4d);
    margin-right: 10px;
    flex: none;
  }
  .services__text {
    display: inline-block;
    height: 38px;
    line-height: 38px;
    padding: 0 20px 0 2px;
    font-size: 30px;
    color: var(--white);
    white-space: nowrap;
    background: linear-gradient(90deg, #0b0000 0%, #000 80%, rgba(0,0,0,0.75) 92%, rgba(60,0,0,0.1) 100%);
    letter-spacing: -0.2px;
    transform: scaleX(var(--condense));
    transform-origin: left center;
  }

  .offer {
    position: absolute;
    left: 18px;
    top: 693px;
    width: 367px;
    height: 172px;
    background: radial-gradient(ellipse 75% 80% at 50% 50%, var(--cream) 60%, #c9a850 82%, var(--maroon-deep) 100%);
    padding: 14px 0 0 44px;
  }
  .offer__copy {
    display: inline-block;
    color: var(--offer-red);
    font-size: 31px;
    line-height: 36px;
    letter-spacing: -0.3px;
    white-space: nowrap;
    transform: scaleX(var(--condense));
    transform-origin: left top;
  }

  .stamp-box {
    position: absolute;
    left: 955px;
    top: 93px;
    width: 141px;
    height: 161px;
    border: 6px solid var(--stamp);
  }
  .address-line {
    position: absolute;
    left: 605px;
    width: 500px;
    height: 6px;
    background-image: radial-gradient(circle, var(--dot) 2.4px, transparent 2.8px);
    background-size: 9.3px 6px;
    background-repeat: repeat-x;
  }
</style>
</head>
<body>
<div class="postcard">
  <svg class="postcard__backdrop" width="1200" height="930" viewBox="0 0 1200 930" aria-hidden="true">
    <defs>
      <linearGradient id="edgeSilver" x1="0" y1="0" x2="1" y2="0">
        <stop offset="0" stop-color="#7d8f8f"/>
        <stop offset="0.45" stop-color="#e4ecec"/>
        <stop offset="1" stop-color="#7d8f8f"/>
      </linearGradient>
    </defs>
    <polygon points="0,0 790,0 270,930 0,930" fill="#860000"/>
    <polygon points="788,0 806,0 276,930 258,930" fill="url(#edgeSilver)"/>
  </svg>

  <p class="pitch">
    <span class="pitch__lead">Let’s be honest:</span> It is impossible to be really good at two things simultaneously.<br>
    Putting focus on one neglects the other and vice versa. Without a lot of outside<br>
    help, running an effective small business AND continuing to be a really<br>
    great appraiser is not really an option. This is where the services of<br>
    The Valuation Desk can help.
  </p>

  <h2 class="services-heading">What we do for you:</h2>
  <ul class="services">
    <li class="services__item"><span class="services__dot"></span><span class="services__text">Answer all of your phone calls.</span></li>
    <li class="services__item"><span class="services__dot"></span><span class="services__text">Set-up all of your appointments.</span></li>
    <li class="services__item"><span class="services__dot"></span><span class="services__text">Answer all of your e-mail.</span></li>
    <li class="services__item"><span class="services__dot"></span><span class="services__text">Update AMC's and Clients.</span></li>
    <li class="services__item"><span class="services__dot"></span><span class="services__text">Update licenses and E&amp;O.</span></li>
    <li class="services__item"><span class="services__dot"></span><span class="services__text">Prep your reports with pertinent data.</span></li>
    <li class="services__item"><span class="services__dot"></span><span class="services__text">Provide plat maps, zoning, field cards &amp;</span></li>
    <li class="services__item"><span class="services__dot"></span><span class="services__text">MLS sheets to your work file.</span></li>
  </ul>

  <div class="offer">
    <p class="offer__copy">
      All for the low introductory<br>
      price&nbsp; of $67 per order.<br>
      Regularly $79<br>
      a 15% savings!!!
    </p>
  </div>

  <div class="stamp-box"></div>
  <div class="address-line" style="top:446px"></div>
  <div class="address-line" style="top:535px"></div>
  <div class="address-line" style="top:614px"></div>
  <div class="address-line" style="top:696px"></div>
</div>
</body>
</html>
```